Important Solar Energy Company Needs a Stationery Design

I need a modern, attractive, corporate stationary design (letter head and business card)
Attached Company Logo

Target Market(s)

Upmarket

Industry/Entity Type

Business

Colors
ec1f27
ffffff
757575
cbcbcb
000000

```html
<!DOCTYPE html>
<html lang="en">
<head>
<meta charset="utf-8">
<title>Solara Prima — Stationery</title>
<link href="https://fonts.googleapis.com/css2?family=Lato:ital,wght@0,400;0,700;1,400&display=swap" rel="stylesheet">
<style>
  :root {
    --brand-red: #ec1f27;
    --folder-red: #d3303a;
    --paper: #f4f4f4;
    --paper-shade: #e9e9e9;
    --backdrop: #dedede;
    --ink-grey: #757575;
    --rule-grey: #cbcbcb;
    --ink-black: #000000;
  }
  * { margin: 0; padding: 0; box-sizing: border-box; }
  html, body { width: 1200px; height: 1000px; overflow: hidden; }
  body {
    background: var(--backdrop);
    font-family: "Lato", sans-serif;
    position: relative;
    color: var(--ink-grey);
  }
  .sheet { position: absolute; overflow: hidden; }
  .diagonal-band { position: absolute; inset: 0; width: 100%; height: 100%; }
  address { font-style: normal; }

  /* Brand lockup: plain circle + name in one weight/colour */
  .brand { display: flex; flex-direction: column; align-items: center; gap: 3px; position: absolute; }
  .brand-dot { width: 22px; height: 22px; border-radius: 50%; background: var(--brand-red); }
  .brand-name { font-weight: 700; font-size: 7px; letter-spacing: 0.6px; color: var(--ink-grey); white-space: nowrap; }
  .brand--on-red .brand-name { color: #ffffff; }

  /* Folder */
  .folder {
    left: 258px; top: 240px; width: 340px; height: 457px;
    background: var(--folder-red);
  }
  .folder .diagonal-band polygon { fill: var(--paper); }
  .folder .brand { right: 20px; top: 18px; }

  /* Letterhead */
  .letterhead {
    left: 628px; top: 255px; width: 312px; height: 442px;
    background: var(--paper);
  }
  .letterhead .diagonal-band polygon { fill: var(--paper-shade); }
  .letterhead .brand { left: 14px; top: 12px; }
  .letterhead-footer {
    position: absolute; left: 190px; bottom: 10px;
    display: flex; gap: 12px; font-size: 4.2px; line-height: 1.45;
  }
  .footer-name { font-weight: 700; font-size: 6px; color: var(--ink-black); letter-spacing: 0.4px; }
  .contact-label { color: var(--brand-red); font-weight: 700; }

  /* Business cards */
  .card { top: 715px; height: 82px; }
  .card-front { left: 648px; width: 129px; background: var(--brand-red); }
  .card-front .diagonal-band polygon { fill: var(--paper); }
  .card-front .brand { right: 10px; bottom: 12px; }
  .card-front .brand-name { font-size: 5.5px; }
  .card-back { left: 793px; width: 126px; background: var(--paper); }
  .card-back .brand { right: 8px; top: 6px; }
  .card-back .brand-dot { width: 14px; height: 14px; }
  .card-back .brand-name { font-size: 5px; }
  .card-person { position: absolute; left: 9px; top: 32px; }
  .person-name { font-size: 6px; color: var(--ink-black); }
  .person-role { font-size: 5.5px; font-style: italic; color: var(--brand-red); }
  .card-details {
    position: absolute; left: 9px; bottom: 6px;
    display: flex; gap: 8px; font-size: 3.6px; line-height: 1.45;
  }
</style>
</head>
<body>
  <section class="sheet folder" aria-label="Presentation folder">
    <svg class="diagonal-band" viewBox="0 0 340 457" preserveAspectRatio="none" aria-hidden="true">
      <polygon points="262,0 340,0 340,40 114,457 90,457"/>
    </svg>
    <div class="brand">
      <span class="brand-dot"></span>
      <span class="brand-name">SOLARAPRIMA</span>
    </div>
  </section>

  <section class="sheet letterhead" aria-label="Letterhead">
    <svg class="diagonal-band" viewBox="0 0 312 442" preserveAspectRatio="none" aria-hidden="true">
      <polygon points="232,0 312,0 312,38 92,442 68,442"/>
    </svg>
    <div class="brand">
      <span class="brand-dot"></span>
      <span class="brand-name">SOLARAPRIMA</span>
    </div>
    <footer class="letterhead-footer">
      <address>
        <div class="footer-name">SOLARAPRIMA</div>
        <div>Via dei Girasoli, 24</div>
        <div>64100 Lido Sereno TE</div>
      </address>
      <div>
        <div><span class="contact-label">Tel:</span> +39 0861 555 010</div>
        <div><span class="contact-label">Fax:</span> +39 0861 555 011</div>
        <div><span class="contact-label">Web:</span> www.solaraprima.it</div>
        <div><span class="contact-label">Email:</span> info@solaraprima.it</div>
      </div>
    </footer>
  </section>

  <section class="sheet card card-front" aria-label="Business card front">
    <svg class="diagonal-band" viewBox="0 0 129 82" preserveAspectRatio="none" aria-hidden="true">
      <polygon points="40,0 76,0 44,82 22,82"/>
    </svg>
    <div class="brand brand--on-red">
      <span class="brand-name">SOLARAPRIMA</span>
    </div>
  </section>

  <section class="sheet card card-back" aria-label="Business card back">
    <div class="brand">
      <span class="brand-dot"></span>
      <span class="brand-name">SOLARAPRIMA</span>
    </div>
    <div class="card-person">
      <div class="person-name">Marco Delvento</div>
      <div class="person-role">Managing Director</div>
    </div>
    <div class="card-details">
      <address>
        <div>Via dei Girasoli, 24</div>
        <div>64100 Lido Sereno TE</div>
      </address>
      <div>
        <div><span class="contact-label">Tel:</span> +39 0861 555 010</div>
        <div><span class="contact-label">Fax:</span> +39 0861 555 011</div>
        <div><span class="contact-label">Web:</span> www.solaraprima.it</div>
        <div><span class="contact-label">Email:</span> info@solaraprima.it</div>
      </div>
    </div>
  </section>
</body>
</html>
```